Create Website for new company called "Verdant Lodge 17"

Verdant Lodge 17 is a new business situated in Southwestern Colorado. We are creating a business that will rent out spaces where clients can grow their own marijuana. Picture a large green house with partitioned spaces that are secured by a lock. Best way to envision this would be to think of a storage business that rents out storage rooms. The difference is that we will be having the units inside a green house ( for growing purposes) Picture a small area that is secured by locks, Picture an area that has the ability to provide state of the art security, cameras etc. We want to focus our efforts on professionals, blue collar workers and end users of marijuana. Our emphasis is in the area of assisting those whom wish to grow their own plants. We want to provide them a safe facility in which to do that. . Keep in mind that we also build custom grow rooms at clients homes and provide a grow pod (lease these) where a small grow unit will be delivered and picked up from our clients whom want to lease a unit for a short amount of time. We have a business card ( just designed) and will send that information to those whom express an interests in this project. We want to be able to sign people up for our services by entering an agreement and signing the agreement while on the internet. We want to provide our services to those whom consume recreational and medical marijuana. This site will need to gather information I.e email addresses so that we can followup with offers. This is a tremendous opportunity for the right designer. We will be creating many more websites as other states come on line and make marijuana legal to consume. Use the business card model for a point of reference of how we envision the concept. That is a business card we just recently printed. The hands and the plant is our logo so far. Open to suggestions. There will be three levels of service. Bronze, Silver, Gold or Platinum. We will also have a retail biz down the road but not at the present time.

Target Market(s)

Ages 21-60

Industry/Entity Type

Medical

Logo Text

Verdant Lodge 17.

Number of Pages Required

5+ page

Requirements
Must have
• Clean appearance not to busy , easily navigable from link to link, page to page. Must have ability down the road to enter into a contractual agreement via the website. Must use our provided logo and example of that is on our business card that will be uploaded here shortly. We would like to have the colors that are on the business card however if you have suggestions or color schemes that you want us to consider that is okay.
Nice to have
• Nice to have a animation of seed to weed and how clients can save a tremendous amount of money growing their own cannabis. Nice to have testimonial page or feedback page. Have a membership component to website,
Should not have
• No flashing lights, etc. Not to busy in terms of animations.

```html
<!DOCTYPE html>
<html lang="en">
<head>
<meta charset="utf-8">
<title>Verdant Lodge 17</title>
<link rel="stylesheet" href="https://fonts.googleapis.com/css2?family=Roboto:wght@400;500;700&family=Roboto+Condensed:wght@700&family=Roboto+Slab:wght@400&display=swap">
<style>
:root{
  --green:#0f7a3a;
  --orange:#c8772a;
  --page:#f0f0f2;
  --ink:#333;
  --footer:#3b4040;
  --white:#fff;
  --line:#c9c9cc;
}
*{box-sizing:border-box;margin:0;padding:0}
html,body{width:886px;height:1200px;overflow:hidden}
body{background:var(--page);font-family:"Roboto",Arial,sans-serif;color:var(--ink);position:relative}
.abs{position:absolute}

.site-header{left:0;top:0;width:886px;height:102px;background:var(--white)}
.brand{left:77px;top:48px;display:flex;align-items:center;gap:7px}
.brand-mark{width:16px;height:16px;border-radius:50%;background:var(--green)}
.brand-name{font-family:"Roboto Condensed",Arial,sans-serif;font-weight:700;font-size:28px;color:#3a3a3a;line-height:1;letter-spacing:-0.3px}
.brand-tagline{left:77px;top:82px;font-family:"Roboto Slab",Georgia,serif;font-size:7.5px;color:#333;white-space:nowrap}
.search{left:714px;top:18px;width:97px;height:29px;border:1px solid #bbb;display:flex;align-items:center;gap:5px;padding-left:9px;font-size:9px;color:#444}
.main-nav{left:387px;top:66px;width:423px;height:36px;background:var(--green);display:flex;border-radius:2px 2px 0 0}
.main-nav a{color:var(--white);text-decoration:none;font-size:10px;font-weight:700;display:flex;align-items:center;justify-content:center;height:100%;position:relative}
.main-nav a.active{background:var(--orange);width:70px}
.main-nav a.item{flex:1}
.main-nav a.item+a.item::before{content:"";position:absolute;left:0;top:11px;height:15px;border-left:1px solid rgba(255,255,255,.25)}

.hero{left:0;top:102px;width:886px;height:388px;
  background:
    radial-gradient(ellipse 160px 120px at 22% 52%,rgba(226,232,120,.85),transparent 70%),
    radial-gradient(ellipse 200px 140px at 52% 30%,rgba(214,222,96,.8),transparent 70%),
    radial-gradient(ellipse 180px 150px at 78% 55%,rgba(220,226,110,.75),transparent 70%),
    radial-gradient(ellipse 140px 90px at 38% 82%,rgba(150,160,40,.8),transparent 70%),
    radial-gradient(ellipse 120px 100px at 92% 18%,rgba(236,238,150,.7),transparent 70%),
    radial-gradient(ellipse 130px 110px at 6% 15%,rgba(120,130,30,.8),transparent 70%),
    linear-gradient(180deg,#8c9a2c 0%,#a4ae3a 40%,#6d7620 100%)}
.hero-arrow{top:275px}
.hero-caption{left:260px;top:420px;width:368px;height:37px;background:rgba(40,40,30,.55);color:var(--white);font-size:13px;display:flex;align-items:center;justify-content:center;letter-spacing:.2px}

.section-title{font-family:"Roboto Condensed",Arial,sans-serif;font-weight:700;font-size:13px;color:var(--green)}
.service{top:528px;width:232px}
.service-photo{width:232px;height:121px;border:3px solid var(--white);box-shadow:0 0 1px #ccc}
.service h3{margin-top:9px;font-family:"Roboto Condensed",Arial,sans-serif;font-size:11px;color:var(--green)}
.service p{margin-top:3px;font-size:9.6px;line-height:12.5px;color:#444;width:206px;height:25px}
.btn{display:inline-flex;align-items:center;justify-content:center;width:44px;height:19px;background:var(--orange);color:var(--white);font-size:8.5px;font-weight:700}
.service .btn{margin-top:7px}

.welcome{left:75px;top:758px;width:736px;height:172px;border:1px solid var(--line)}
.welcome-lead{left:13px;top:19px;width:468px;font-size:10.4px;font-weight:500;line-height:13.5px;color:#333}
.welcome-body{left:13px;top:52px;width:476px;font-size:9.6px;line-height:13.6px;color:#555}
.welcome .btn{left:13px;top:129px;position:absolute}
.welcome-photo{left:528px;top:42px;width:192px;height:113px;
  background:
    radial-gradient(ellipse 50px 40px at 50% 58%,#7cf04a,transparent 75%),
    radial-gradient(ellipse 70px 30px at 30% 40%,rgba(70,200,50,.6),transparent 75%),
    radial-gradient(ellipse 70px 30px at 72% 40%,rgba(70,200,50,.6),transparent 75%),
    radial-gradient(circle at 50% 55%,#2a9a22 0%,#0d5a14 60%,#04300a 100%)}

.greenhouse{left:75px;top:938px;width:736px;height:174px;background:var(--green)}
.greenhouse h2{left:21px;top:18px;font-family:"Roboto Condensed",Arial,sans-serif;font-size:13px;color:var(--white)}
.greenhouse p{left:21px;top:40px;width:348px;font-size:9.6px;line-height:13.6px;color:var(--white)}
.greenhouse .btn{position:absolute;left:23px;top:131px}
.greenhouse-photo{left:400px;top:0;width:336px;height:174px;
  background:
    radial-gradient(ellipse 150px 40px at 55% 62%,rgba(210,220,215,.85),transparent 75%),
    radial-gradient(ellipse 60px 14px at 30% 88%,rgba(170,130,80,.8),transparent 80%),
    radial-gradient(ellipse 60px 14px at 68% 90%,rgba(170,130,80,.8),transparent 80%),
    radial-gradient(ellipse 120px 50px at 20% 15%,rgba(40,100,30,.9),transparent 75%),
    radial-gradient(ellipse 120px 50px at 80% 10%,rgba(90,140,60,.9),transparent 75%),
    linear-gradient(180deg,#3f7a2e 0%,#5f8f45 40%,#9aa8a0 58%,#7fb83a 78%,#93c744 100%)}

.site-footer{left:0;top:1118px;width:886px;height:82px;background:var(--footer);color:var(--white)}
.follow{left:78px;top:20px;font-size:9px;font-weight:700}
.social{left:78px;top:38px;display:flex;gap:8px}
.social span{width:17px;height:17px;background:#2f6fb0;border-radius:2px}
.footer-nav{right:69px;top:20px;font-size:9px;display:flex;gap:7px}
.copyright{right:69px;top:39px;font-size:8.6px}
</style>
</head>
<body>

<header class="site-header abs">
  <div class="brand abs"><span class="brand-mark"></span><span class="brand-name">VERDANT LODGE 17</span></div>
  <div class="brand-tagline abs">“supporting the care &amp; cultivation of cannabis”</div>
  <div class="search abs">
    <svg width="9" height="9" viewBox="0 0 10 10"><circle cx="4" cy="4" r="3" fill="none" stroke="#444" stroke-width="1.4"/><line x1="6.3" y1="6.3" x2="9" y2="9" stroke="#444" stroke-width="1.4"/></svg>
    SEARCH
  </div>
  <nav class="main-nav abs">
    <a class="active">HOME</a>
    <a class="item">ABOUT US</a>
    <a class="item">SERVICES</a>
    <a class="item">CANNABIS</a>
    <a class="item">CONTACT US</a>
  </nav>
</header>

<section class="hero abs" role="img" aria-label="Close-up of green cannabis leaves in soft light"></section>
<svg class="hero-arrow abs" style="left:60px" width="26" height="44" viewBox="0 0 26 44"><polyline points="22,3 4,22 22,41" fill="none" stroke="#fff" stroke-width="5"/></svg>
<svg class="hero-arrow abs" style="left:800px" width="26" height="44" viewBox="0 0 26 44"><polyline points="4,3 22,22 4,41" fill="none" stroke="#fff" stroke-width="5"/></svg>
<div class="hero-caption abs">SUPPORTING THE CARE &amp; CULTIVATION OF CANNABIS</div>

<h2 class="section-title abs" style="left:75px;top:506px">OUR SERVICES</h2>

<article class="service abs" style="left:75px">
  <div class="service-photo" role="img" aria-label="Dense bright green cannabis leaves" style="background:radial-gradient(ellipse 50px 30px at 20% 30%,#6bd048,transparent 75%),radial-gradient(ellipse 60px 30px at 70% 60%,#5cc43a,transparent 75%),radial-gradient(ellipse 40px 25px at 50% 15%,#1c6e18,transparent 75%),radial-gradient(ellipse 50px 25px at 85% 20%,#7ad650,transparent 75%),linear-gradient(135deg,#2f9a24,#1d7a1a 60%,#46ae30)"></div>
  <h3>LOREM IPSUM IS SIMPLY</h3>
  <p>Contrary to popular belief, Lorem Ipsum is not simply random text</p>
  <span class="btn">MORE</span>
</article>
<article class="service abs" style="left:327px">
  <div class="service-photo" role="img" aria-label="Rows of cannabis plants growing in a field" style="background:radial-gradient(ellipse 40px 30px at 25% 70%,#9a8a6a,transparent 75%),radial-gradient(ellipse 50px 30px at 70% 80%,#a08e70,transparent 75%),radial-gradient(ellipse 60px 35px at 40% 30%,#7a9a50,transparent 75%),radial-gradient(ellipse 60px 35px at 85% 35%,#5e7e3c,transparent 75%),linear-gradient(160deg,#5a7a3e,#4d6a32 50%,#6e7a4a)"></div>
  <h3>THE STANDARD CHUNK OF</h3>
  <p>There are many variations of passages of Lorem Ipsum available, but the majority have suffered .</p>
  <span class="btn">MORE</span>
</article>
<article class="service abs" style="left:580px">
  <div class="service-photo" role="img" aria-label="Young seedling sprouting from dark soil" style="background:radial-gradient(ellipse 40px 22px at 66% 28%,#5fb83a,transparent 80%),radial-gradient(ellipse 8px 40px at 62% 78%,#4c8a2a,transparent 80%),radial-gradient(circle at 60% 40%,#2c3a22 0%,#2a2a22 40%,#1a1814 100%)"></div>
  <h3>THE STANDARD CHUNK OF LOREM</h3>
  <p>Cicero are also reproduced in their exact original form, accompanied by English versions.</p>
  <span class="btn">MORE</span>
</article>

<h2 class="section-title abs" style="left:75px;top:739px">WELCOME TO OUR SITE</h2>
<section class="welcome abs">
  <p class="welcome-lead abs">It is a long established fact that a reader will be distracted by the readable content of a page when looking at its layout. The point of using Lorem Ipsum is.</p>
  <p class="welcome-body abs">At vero eos et accusamus et iusto odio dignissimos ducimus qui blanditiis praesentium voluptatum deleniti atque corrupti quos dolores et quas molestias excepturi sint occaecati cupiditate non provident,similique sunt in culpa qui officia deserunt mollitia animi, id est laborum et dolorum fuga. Et harum quidem rerum facilis.&nbsp; est et expedita distinctio. Nam libero tempore, cum soluta nobis est eligendi optio cumque nihil impedit quo minus id quod maxime placeat facere possimus.</p>
  <span class="btn">MORE</span>
  <div class="welcome-photo abs" role="img" aria-label="Single bright green cannabis leaf on a dark green background"></div>
</section>

<section class="greenhouse abs">
  <h2 class="abs">GREEN HOUSE</h2>
  <p class="abs">Contrary to popular belief, Lorem Ipsum is not simply random text. It has roots in a piece of classical Latin literature from 45 BC, making it over 2000 years old. Howard Pellman, a Latin professor at Ashford Ridge College in Virginia, looked up one of the more obscure Latin words, consectetur, from a Lorem Ipsum passage, and going through the cites of the word in classical literature, discovered the undoubtable source</p>
  <span class="btn">MORE</span>
  <div class="greenhouse-photo abs" role="img" aria-label="Glass greenhouse surrounded by trees with planters on a lawn"></div>
</section>

<footer class="site-footer abs">
  <div class="follow abs">FOLLOW US ON</div>
  <div class="social abs"><span></span><span style="background:#3fa9e0"></span><span style="background:#1d7bb8"></span></div>
  <nav class="footer-nav abs">
    <span>HOME</span><span>|</span><span>ABOUT US</span><span>|</span><span>SERVICES</span><span>|</span><span>PRODUCTS</span><span>|</span><span>BLOG</span><span>|</span><span>CONTACT US</span>
  </nav>
  <div class="copyright abs">COPYRIGHTS @ 2014 ALL RIGHTS RESERVED</div>
</footer>

</body>
</html>
```